TPR Letterhead

We need a letterhead design that will be able to be used on all marketing products (letterhead, mail chimp, envelops, business cards, etc.) We are a law firm specializing primarily in transportation law but offer a wide range of services to our clients. We would like the design to be modern, simple, and professional. Our colors are black and gold, however, we've incorporated dark gray and white on other marketing products such as our website.

```html
<!DOCTYPE html>
<html lang="en">
<head>
<meta charset="utf-8">
<title>TPR Law Group Letterhead</title>
<link rel="stylesheet" href="https://fonts.googleapis.com/css2?family=Cinzel:wght@400&family=Open+Sans:wght@400&display=swap">
<style>
  :root {
    --paper: #ffffff;
    --ink: #111111;
    --gold: #b39a6e;
    --grey-text: #4a4a4a;
    --icon: #8a8a8a;
  }
  * { margin: 0; padding: 0; box-sizing: border-box; }
  html, body {
    width: 1058px;
    height: 1200px;
    overflow: hidden;
    background: var(--paper);
  }
  .letterhead {
    position: relative;
    width: 1058px;
    height: 1200px;
    background: var(--paper);
  }
  .brand {
    position: absolute;
    left: 38px;
    top: 96px;
    display: flex;
    align-items: center;
    gap: 12px;
  }
  .brand-square {
    width: 22px;
    height: 22px;
    background: var(--gold);
  }
  .brand-name {
    font-family: "Cinzel", serif;
    font-weight: 400;
    font-size: 34px;
    letter-spacing: 1px;
    color: var(--ink);
    line-height: 1;
  }
  .contact {
    position: absolute;
    left: 819px;
    top: 62px;
    font-family: "Open Sans", sans-serif;
    color: var(--grey-text);
  }
  .contact-firm {
    font-size: 18px;
    color: var(--gold);
    margin-bottom: 6px;
  }
  .contact-address {
    font-size: 13px;
    line-height: 17px;
    margin-bottom: 8px;
  }
  .contact-list { list-style: none; }
  .contact-list li {
    display: flex;
    align-items: center;
    gap: 8px;
    font-size: 13px;
    line-height: 20px;
  }
  .contact-list svg { width: 12px; height: 12px; flex: none; }
  .corner-accent {
    position: absolute;
    right: 0;
    bottom: 0;
    width: 176px;
    height: 154px;
  }
</style>
</head>
<body>
  <main class="letterhead">
    <header class="brand">
      <span class="brand-square"></span>
      <span class="brand-name">TPR Law Group</span>
    </header>

    <address class="contact">
      <p class="contact-firm">TPR Law Group</p>
      <p class="contact-address">240 Harbor View Avenue, Suite<br>310 Riverton, FL 33010</p>
      <ul class="contact-list">
        <li>
          <svg viewBox="0 0 12 12" aria-hidden="true"><path fill="var(--icon)" d="M2.5 1 4.5 1 5.2 3.4 4 4.4C4.7 5.9 6 7.2 7.6 8L8.6 6.8 11 7.5 11 9.5C11 10.3 10.3 11 9.5 11 5 11 1 7 1 2.5 1 1.7 1.7 1 2.5 1Z"/></svg>
          555.014.2290
        </li>
        <li>
          <svg viewBox="0 0 12 12" aria-hidden="true"><rect x="1" y="2.5" width="10" height="7" fill="none" stroke="var(--icon)" stroke-width="1.2"/><path d="M1 2.5 6 6.5 11 2.5" fill="none" stroke="var(--icon)" stroke-width="1.2"/></svg>
          admin@tprlawgroup.com
        </li>
        <li>
          <svg viewBox="0 0 12 12" aria-hidden="true"><circle cx="6" cy="6" r="5" fill="none" stroke="var(--icon)" stroke-width="1"/><ellipse cx="6" cy="6" rx="2.2" ry="5" fill="none" stroke="var(--icon)" stroke-width="1"/><path d="M1 6H11" stroke="var(--icon)" stroke-width="1"/></svg>
          www.tprlawgroup.com
        </li>
      </ul>
    </address>

    <svg class="corner-accent" viewBox="0 0 176 154" aria-hidden="true">
      <polygon points="0,154 176,154 176,0" fill="var(--ink)"/>
    </svg>
  </main>
</body>
</html>
```